UPDATED BRIEF: We are looking for a trade show booth design - The design is for 10ft x 10 ft booth curved booth display.
we want to utilize the laptop image more with a half wheel of the key services on our platform.
Strategic DEI Business Partner Workshops
Leader to Leader Training
ERG Leader Strategic Training
15 - Microlearning Labs
Coaching & Mentorship
DEI Research, Articles and Hot topics

With the tagline: Experience the Power of Strategic DEI Training and Peer-to-Peer Support on One Platform

About us: we are a learning and development community for diversity and inclusion and talent management professionals. Our corporate colors are blue, 004AAD
We are looking for a clean, corporate design that makes someone feel included. The moment you look at it, you feel included. We may add a screenshot of the Brightpath Growth Studio platform. Our logo will be included and our tagline is

"Together We Can Create a More Inclusive Future: The Brightpath Growth Studio Community for DEI and Talent Leaders."

We have two versions of our logo - one with text only the other with the logo design. We're not sure which one we want to use.

Target Market(s)

Human Resources and Talent Leaders

Industry/Entity Type

Training and development

Colors
0054AA
0677BA
7BADD7
CADEEF
E8F1F8
F0912C
F2A743
F7CA91
FBE8D2
FDF5EE
EB3D1F
EC4F4E
F09395
F8D3D4
FCEDEE

Requirements
Must have
• Must have logo and good visual design
Should not have
• I've added the examples of what I am looking for

```html
<!DOCTYPE html>
<html lang="en">
<head>
<meta charset="utf-8">
<title>Brightpath Growth Studio – Booth Panel</title>
<link rel="stylesheet" href="https://fonts.googleapis.com/css2?family=Poppins:wght@400;500;600;700;800&display=swap">
<style>
  :root {
    --navy: #0b1a48;
    --red: #cd1b22;
    --white: #ffffff;
    --page: #d9d9d9;
    --room-light: #f2f2f2;
    --room-mid: #d4d4d4;
    --ink: #14213d;
  }
  * { margin: 0; padding: 0; box-sizing: border-box; }
  html, body { width: 690px; height: 1200px; overflow: hidden; background: var(--page); }
  body { position: relative; font-family: "Poppins", sans-serif; }

  .booth-panel {
    position: absolute; left: 0; top: 255px;
    width: 690px; height: 690px; overflow: hidden;
  }
  .room-backdrop {
    position: absolute; inset: 0;
    background: radial-gradient(ellipse at 55% 40%, var(--room-light) 0%, #e4e4e4 55%, var(--room-mid) 100%);
  }
  .footer-band {
    position: absolute; left: 0; top: 523px; width: 690px; height: 167px;
    background: var(--navy);
  }
  .brand-mark {
    position: absolute; left: 40px; top: 70px;
    display: flex; align-items: center; gap: 8px;
  }
  .brand-dot { width: 16px; height: 16px; border-radius: 50%; background: var(--red); flex: none; }
  .brand-name {
    font-weight: 700; font-size: 17px; line-height: 1.1; color: var(--red); width: 120px;
  }
  .wheel { position: absolute; left: 0; top: 0; }

  .hero-copy {
    position: absolute; left: 53px; top: 226px; width: 258px;
    text-align: center; color: var(--white);
  }
  .hero-copy .lead { font-size: 13px; font-weight: 400; line-height: 1; }
  .hero-copy .power { font-size: 17.5px; font-weight: 700; line-height: 1; margin-top: 5px; }
  .hero-copy .dei { font-size: 29px; font-weight: 800; color: var(--red); line-height: 1; margin-top: 2px; letter-spacing: -0.3px; }
  .hero-copy .peer { font-size: 16.5px; font-weight: 700; line-height: 1; margin-top: 2px; }
  .hero-copy .platform {
    display: inline-block; margin-top: 5px; padding: 1px 6px;
    background: var(--red); font-size: 11.5px; font-weight: 600; line-height: 15px;
  }

  .service {
    position: absolute; height: 48px; width: 226px;
    border-radius: 14px; padding-left: 20px;
    display: flex; align-items: center;
    font-size: 14px; font-weight: 600; line-height: 1.15;
    box-shadow: 3px 3px 0 var(--red);
  }
  .service.dark { background: var(--navy); color: var(--white); }
  .service.light { background: var(--white); color: var(--ink); }
  .service.compact {
    padding-left: 12px; font-size: 12.8px; letter-spacing: -0.2px; white-space: nowrap;
  }

  .laptop {
    position: absolute; left: 47px; top: 480px; width: 211px; height: 118px;
  }
  .laptop-screen {
    position: absolute; left: 20px; top: 0; width: 172px; height: 112px;
    border: 3px solid #111; border-radius: 5px;
    background: linear-gradient(135deg, #eef1f6 0%, #c9d3e3 60%, #8fa0bf 100%);
  }
  .laptop-base {
    position: absolute; left: 0; top: 112px; width: 211px; height: 5px;
    border-radius: 0 0 6px 6px; background: linear-gradient(#b9bcc2, #6f737a);
  }
  .footer-copy { position: absolute; left: 264px; top: 545px; color: var(--white); }
  .footer-copy .tagline { font-size: 12.5px; font-weight: 700; letter-spacing: 0.1px; }
  .footer-copy .web { font-size: 21.5px; font-weight: 700; line-height: 1.2; }
  .footer-copy .web span { color: var(--red); }
</style>
</head>
<body>
<main class="booth-panel">
  <div class="room-backdrop" role="img" aria-label="Soft grey photo of an empty training room"></div>
  <div class="footer-band"></div>

  <div class="brand-mark">
    <span class="brand-dot"></span>
    <span class="brand-name">Brightpath Growth Studio</span>
  </div>

  <svg class="wheel" width="690" height="523" viewBox="0 0 690 523" aria-hidden="true">
    <path d="M182 69 A196 196 0 0 1 182 461 Z" fill="#cd1b22"/>
    <circle cx="182" cy="265" r="140" fill="#fff"/>
    <circle cx="182" cy="265" r="129" fill="#0b1a48"/>

    <!-- presenter with stars -->
    <g fill="none" stroke="#cd1b22" stroke-width="2" stroke-linejoin="round">
      <circle cx="182" cy="172" r="6"/>
      <path d="M172 200 v-12 a10 10 0 0 1 20 0 v12"/>
      <path d="M182 197 l3 6 6 1 -4.5 4 1 6 -5.5 -3 -5.5 3 1 -6 -4.5 -4 6 -1z"/>
      <path d="M165 203 l2.5 5 5 .8 -3.7 3.4 .9 5 -4.7 -2.5 -4.7 2.5 .9 -5 -3.7 -3.4 5 -.8z"/>
      <path d="M199 203 l2.5 5 5 .8 -3.7 3.4 .9 5 -4.7 -2.5 -4.7 2.5 .9 -5 -3.7 -3.4 5 -.8z"/>
    </g>

    <!-- service icons -->
    <g stroke="#fff" stroke-width="2.5">
      <circle cx="300" cy="101" r="23" fill="#0b1a48"/>
      <circle cx="351" cy="160" r="23" fill="#0b1a48"/>
      <circle cx="373" cy="229" r="23" fill="#0b1a48"/>
      <circle cx="373" cy="297" r="23" fill="#0b1a48"/>
      <circle cx="351" cy="363" r="23" fill="#0b1a48"/>
      <circle cx="300" cy="424" r="23" fill="#0b1a48"/>
    </g>
    <g fill="none" stroke="#fff" stroke-width="1.3" stroke-linecap="round">
      <circle cx="300" cy="101" r="8"/><circle cx="300" cy="101" r="3"/>
      <path d="M300 89v4M300 109v4M288 101h4M308 101h4M292 93l3 3M305 106l3 3M308 93l-3 3M295 106l-3 3"/>
      <rect x="340" y="150" width="22" height="13" rx="1"/><path d="M344 159l4-4 3 3 5-5M345 170v-4M351 170v-4M357 170v-4"/>
      <circle cx="373" cy="219" r="3"/><path d="M368 228a5 5 0 0 1 10 0M363 238a4 4 0 0 1 8 0M375 238a4 4 0 0 1 8 0M367 232v-2h12v2"/>
      <circle cx="373" cy="293" r="6"/><path d="M373 299v8M368 307h10M364 287l3 2M382 287l-3 2M373 283v3"/>
      <rect x="346" y="352" width="16" height="11" rx="1"/><path d="M349 356h10M349 359h7M342 374v-4a3 3 0 0 1 6 0v4M355 374v-3a2.5 2.5 0 0 1 5 0v3"/><circle cx="345" cy="364" r="2.5"/>
      <rect x="291" y="414" width="16" height="20" rx="1"/><path d="M294 419h10M294 423h10M294 427h6"/><circle cx="305" cy="430" r="4"/><path d="M308 433l3 3"/>
    </g>
  </svg>

  <div class="hero-copy">
    <p class="lead">EXPERIENCE THE</p>
    <p class="power">POWER OF STRATEGIC</p>
    <p class="dei">DEI TRAINING</p>
    <p class="peer">&amp; PEER-TO-PEER</p>
    <p class="platform">SUPPORTON ONE PLATFORM</p>
  </div>

  <div class="service dark" style="left:349px;top:62px;">Strategic DEI Business<br>Partner Workshops</div>
  <div class="service light" style="left:385px;top:131px;">Leader to Leader Training</div>
  <div class="service dark compact" style="left:418px;top:201px;">ERG Leader Strategic Training</div>
  <div class="service light" style="left:418px;top:269px;">15 - Microlearning Labs</div>
  <div class="service dark" style="left:385px;top:339px;">Coaching &amp; Mentorship</div>
  <div class="service light" style="left:349px;top:408px;">DEI Research, Articles and<br>Hot topics</div>

  <div class="laptop">
    <div class="laptop-screen" role="img" aria-label="Laptop showing the learning platform webinar library"></div>
    <div class="laptop-base"></div>
  </div>

  <div class="footer-copy">
    <p class="tagline">TOGETHER WE CAN CREATE A MORE INCLUSIVE FUTURE</p>
    <p class="web">www.<span>brightpathgrowthstudio</span>.com</p>
  </div>
</main>
</body>
</html>
```